Valdorick Business Card Design

Valdorick is the holdings company for my portfolio of businesses. These businesses currently only include Valdorick Advising. V|A is a strategic consulting firm that focuses on small businesses and start-ups that want help with their brand. We focus on partnering with influencers (Pro Athletes and Celebrities) and Social Media Marketing. We also want to focus on companies that have a positive effect on the community or world. The audience I am going after is very corporate. I want to have the corporate edge with some 25yr old flair.
Industry/Entity Type
Business
Contact Information for Business Card
General Idea AttachedLogo (Attached)Jonathan R. MasonCEO & Managing MemberDown Left Bottom CornerPhone: 347-570-0585Cell: 240-604-7930mason@valdorick-example.comDown Right Bottom Corner 174 W 4th St, Ste 212New York, NY 10014www.valdorick-example.comBackside LogoI want the entire card extra thick and with metallic finish
Look and feel

```html
<!DOCTYPE html>
<html lang="en">
<head>
<meta charset="utf-8">
<title>Valdorick Holdings Business Card</title>
<link href="https://fonts.googleapis.com/css2?family=Tinos:ital,wght@0,400;0,700;1,400&display=swap" rel="stylesheet">
<style>
  :root {
    --backdrop: #e4e2df;
    --card: #f7f7f7;
    --card-edge: #e2e2e2;
    --brand-red: #a3172a;
    --ink: #5a5a5a;
    --ink-soft: #7a7a7a;
    --rule: #c9c9c9;
  }
  * { box-sizing: border-box; margin: 0; padding: 0; }
  html, body { width: 1200px; height: 1091px; overflow: hidden; }
  body {
    background: var(--backdrop);
    font-family: "Tinos", "Times New Roman", serif;
    color: var(--ink);
    position: relative;
  }
  .card {
    position: absolute;
    left: 320px;
    width: 560px;
    height: 320px;
    background: linear-gradient(160deg, #ffffff 0%, var(--card) 60%, var(--card-edge) 100%);
    box-shadow: 0 10px 28px rgba(0,0,0,0.18);
  }
  .card--front { top: 195px; }
  .card--back { top: 575px; }

  .brand { position: absolute; display: flex; align-items: center; }
  .brand__square { background: var(--brand-red); flex: none; }
  .brand__text { display: flex; flex-direction: column; align-items: flex-end; }
  .brand__name {
    color: var(--brand-red);
    font-weight: 400;
    text-transform: uppercase;
    letter-spacing: 0.06em;
    white-space: nowrap;
    line-height: 1.1;
  }
  .brand__llc {
    color: var(--ink-soft);
    letter-spacing: 0.15em;
    line-height: 1;
    margin-top: 2px;
  }

  .card--front .brand { left: 70px; top: 128px; gap: 22px; }
  .card--front .brand__square { width: 60px; height: 60px; }
  .card--front .brand__text { border-bottom: 1px solid var(--rule); padding-bottom: 4px; }
  .card--front .brand__name { font-size: 28px; }
  .card--front .brand__llc { font-size: 10px; }

  .card--back .brand { left: 40px; top: 36px; gap: 16px; }
  .card--back .brand__square { width: 42px; height: 42px; }
  .card--back .brand__name { font-size: 20px; }
  .card--back .brand__llc { font-size: 8px; }
  .card--back .brand__rule { position: absolute; left: 98px; top: 82px; width: 422px; height: 1px; background: var(--rule); }

  .person { position: absolute; left: 40px; top: 110px; }
  .person__name { font-size: 22px; font-weight: 700; color: var(--ink); }
  .person__title { font-size: 13px; font-style: italic; color: var(--ink-soft); margin-top: 3px; }

  .address { position: absolute; left: 40px; top: 178px; font-size: 13px; color: var(--ink-soft); }

  .contact-list { position: absolute; list-style: none; font-size: 13px; color: var(--ink-soft); }
  .contact-list li { display: flex; align-items: center; gap: 9px; height: 21px; }
  .contact-list svg { width: 12px; height: 12px; fill: var(--ink); flex: none; }
  .contact-list--phones { left: 40px; top: 222px; }
  .contact-list--web { left: 320px; top: 110px; }
</style>
</head>
<body>
  <section class="card card--front" aria-label="Card front">
    <div class="brand">
      <span class="brand__square"></span>
      <div class="brand__text">
        <span class="brand__name">Valdorick Holdings</span>
        <span class="brand__llc">LLC</span>
      </div>
    </div>
  </section>

  <section class="card card--back" aria-label="Card back">
    <div class="brand">
      <span class="brand__square"></span>
      <div class="brand__text">
        <span class="brand__name">Valdorick Holdings</span>
        <span class="brand__llc">LLC</span>
      </div>
    </div>
    <span class="brand__rule"></span>

    <div class="person">
      <p class="person__name">Derrick Fanshaw</p>
      <p class="person__title">CEO Managing Member</p>
    </div>

    <p class="address">88 E 9th St, Ste 405, New York, NY 10099</p>

    <ul class="contact-list contact-list--phones">
      <li>
        <svg viewBox="0 0 12 12" aria-hidden="true"><path d="M1 4c0-2 2-3 5-3s5 1 5 3l-2 1-1-2H4L3 5zM2 6h8l1 5H1z"/></svg>
        <span>347-555-0162</span>
      </li>
      <li>
        <svg viewBox="0 0 12 12" aria-hidden="true"><path d="M3 0h6v12H3zM4 1.5v8h4v-8z"/></svg>
        <span>240-555-0187</span>
      </li>
    </ul>

    <ul class="contact-list contact-list--web">
      <li>
        <svg viewBox="0 0 12 12" aria-hidden="true"><path d="M6 0a6 6 0 1 0 0 12A6 6 0 0 0 6 0zm0 1.3c.8.8 1.4 2.2 1.5 3.7h-3C4.6 3.5 5.2 2.1 6 1.3zM1.3 6.8h2c.1 1.4.5 2.6 1.1 3.5A4.8 4.8 0 0 1 1.3 6.8zm0-1.6a4.8 4.8 0 0 1 3.1-3.5c-.6.9-1 2.1-1.1 3.5zm3.2 1.6h3c-.1 1.5-.7 2.9-1.5 3.7-.8-.8-1.4-2.2-1.5-3.7zm4.2 0h2a4.8 4.8 0 0 1-3.1 3.5c.6-.9 1-2.1 1.1-3.5zm0-1.6c-.1-1.4-.5-2.6-1.1-3.5a4.8 4.8 0 0 1 3.1 3.5z"/></svg>
        <span>www.valdorick-example.com</span>
      </li>
      <li>
        <svg viewBox="0 0 12 12" aria-hidden="true"><path d="M0 2h12v8H0zm1 1v.3l5 3.2 5-3.2V3zm0 1.5V9h10V4.5L6 7.7z"/></svg>
        <span>fanshaw@valdorick-example.com</span>
      </li>
    </ul>
  </section>
</body>
</html>
```